20 year old business card needs re-design

We need to redesign our corporate business card look. We need something that appears more modern, eye catchy but professional.

Target Market(s)

manufacturing industry

Industry/Entity Type

Manufacturer

Contact Information for Business Card

One side can have the logo. Other side can have contact information.

Font styles to use
Serif

Colors
3277b5
33b8a4
ffffff

Requirements
Must have
• Eye catchy - need to standout from the crowd. company logo cannot change. Full name, job title, phone number and email address.
Should not have
• Fax, business address is not necessary.

```html
<!DOCTYPE html>
<html lang="en">
<head>
<meta charset="utf-8">
<title>Norvale Industrial – Business Card</title>
<link rel="stylesheet" href="https://fonts.googleapis.com/css2?family=Libre+Baskerville:wght@700&family=Roboto:wght@400;700&display=swap">
<style>
  :root {
    --blue: #3277b5;
    --teal: #33b8a4;
    --white: #ffffff;
    --ink: #1c1c1c;
    --card-black: #131415;
    --backdrop: #2b2b2c;
    --muted: #555a60;
  }
  * { margin: 0; padding: 0; box-sizing: border-box; }
  html, body {
    width: 1200px; height: 834px; overflow: hidden;
    background: var(--backdrop);
    font-family: "Roboto", Arial, sans-serif;
  }
  .stage {
    width: 1200px; height: 834px;
    display: flex; align-items: center; justify-content: center; gap: 50px;
  }
  .card {
    position: relative;
    width: 525px; height: 300px;
    overflow: hidden;
    box-shadow: 0 12px 30px rgba(0,0,0,.45);
  }
  /* Front */
  .card--front { background: var(--card-black); }
  .card--front .wordmark {
    position: absolute; top: 98px; left: 0; right: 0;
    text-align: center;
    color: var(--teal);
  }
  .wordmark {
    font-family: "Roboto", Arial, sans-serif;
    font-weight: 700; font-size: 40px; letter-spacing: -0.5px;
  }
  .tagline {
    position: absolute; top: 180px; left: 0; right: 0;
    text-align: center;
    color: #6fa9dc;
    font-size: 11px; line-height: 14px;
  }
  .front-band {
    position: absolute; left: 0; right: 0; top: 216px; height: 38px;
    background: var(--blue);
  }
  /* Back */
  .card--back { background: var(--white); }
  .card--back .wordmark {
    position: absolute; top: 62px; left: 0; right: 0;
    text-align: center;
    color: var(--ink);
  }
  .holder {
    position: absolute; left: 48px; top: 196px;
  }
  .holder__name {
    font-family: "Libre Baskerville", Georgia, serif;
    font-weight: 700; font-size: 15px; color: #333;
  }
  .holder__title { font-size: 11px; color: var(--blue); margin-top: 2px; }
  .contacts {
    position: absolute; left: 268px; top: 168px;
    list-style: none;
  }
  .contacts li {
    display: flex; align-items: center; gap: 10px;
    font-size: 11px; color: var(--muted);
    height: 22px;
  }
  .contacts svg { width: 13px; height: 13px; flex: none; }
  .back-band {
    position: absolute; left: 0; right: 0; bottom: 0; height: 22px;
    background: var(--blue);
  }
</style>
</head>
<body>
<main class="stage">
  <section class="card card--front" aria-label="Business card front">
    <div class="wordmark">Norvale Industrial</div>
    <p class="tagline">International Manufacturing Solutions for OEM<br>customers in North America</p>
    <div class="front-band"></div>
  </section>

  <section class="card card--back" aria-label="Business card back">
    <div class="wordmark">Norvale Industrial</div>
    <div class="holder">
      <p class="holder__name">Daniel Marrow</p>
      <p class="holder__title">President</p>
    </div>
    <ul class="contacts">
      <li>
        <svg viewBox="0 0 16 16" fill="none" stroke="var(--blue)" stroke-width="1.4" aria-hidden="true"><path d="M3 2h3l1.5 3.5-2 1.2a8 8 0 0 0 3.8 3.8l1.2-2L14 10v3a1 1 0 0 1-1 1A11 11 0 0 1 2 3a1 1 0 0 1 1-1z"/></svg>
        555-014-2200 x201
      </li>
      <li>
        <svg viewBox="0 0 16 16" fill="none" stroke="var(--blue)" stroke-width="1.4" aria-hidden="true"><rect x="1.5" y="3.5" width="13" height="9"/><path d="M1.5 3.5 8 9l6.5-5.5"/></svg>
        dan@norvaleindustrial.com
      </li>
      <li>
        <svg viewBox="0 0 16 16" fill="none" stroke="var(--blue)" stroke-width="1.4" aria-hidden="true"><circle cx="8" cy="8" r="6.3"/><ellipse cx="8" cy="8" rx="2.8" ry="6.3"/><path d="M1.7 8h12.6"/></svg>
        www.norvaleindustrial.com
      </li>
    </ul>
    <div class="back-band"></div>
  </section>
</main>
</body>
</html>
```